Employee Portal UI Design - Modern and Clean

We are an agency tasked with developing a team portal for a company that has many employees. As we embark on this project, we seek a great UI design to accompany the requirements our client has for this project. We already have several screens mocked up that can be used as reference for the overall idea. Currently, we are only looking for the main dashboard's home page, user registration screen, and account settings page to be designed. The main brand colors are red but other accents can be used as well. The client's vision is for modern & minimalist to be at the center. We have a specific font to be used, but if you don't have access to it, you can just use a similar font.Main color: #DD0031The sub menus (do not need to be designed) would be:>Performance Reviews>Posts>Team directory>Calendar>Tasks>Documents>LinksWe would prefer the design be made in Adobe XD.

Industry/Entity Type

Fast Food Restaurant

Number of Pages Required

1 page

Font styles to use
Sans Serif

Colors
ec1f27

Requirements
Must have
• Color: #DD0031 (highlights)

```html
<!DOCTYPE html>
<html lang="en">
<head>
<meta charset="utf-8">
<title>Tablehub – Home</title>
<link rel="stylesheet" href="https://fonts.googleapis.com/css2?family=Roboto:wght@300;400;500;700&display=swap">
<style>
:root{
  --brand:#e8141c;
  --brand-deep:#c8161d;
  --ink:#2b2d33;
  --muted:#8b9099;
  --soft:#5f6b7a;
  --line:#e9ebef;
  --page:#f3f4f7;
  --card:#ffffff;
  --green:#6ccc5a;
  --cyan:#5bcbef;
  --orange:#e8890c;
  --amber:#f5a623;
}
*{box-sizing:border-box;margin:0;padding:0}
html,body{width:1200px;height:1054px;overflow:hidden}
body{font-family:"Roboto",Arial,sans-serif;background:var(--page);color:var(--ink);position:relative}
.topbar{position:absolute;left:0;top:0;width:1200px;height:65px;background:#fff}
.brand{position:absolute;left:21px;top:14px;font-size:25px;font-weight:400;color:var(--brand);letter-spacing:-.3px}
.topbar .bell{position:absolute;left:873px;top:19px}
.topbar .gear{position:absolute;left:915px;top:20px}
.user-name{position:absolute;left:953px;top:22px;font-size:16px;font-weight:300;color:var(--ink)}
.user-avatar{position:absolute;left:1054px;top:15px;width:35px;height:35px;border-radius:50%;background:linear-gradient(135deg,#6f7c86,#3b3f45)}
.user-avatar::after{content:"";position:absolute;right:1px;top:1px;width:6px;height:6px;border-radius:50%;background:#2fd3a0}
.sidebar{position:absolute;left:0;top:65px;width:73px;height:989px;background:#fff;border-left:2px solid #eceef2}
.nav-home{position:absolute;left:0;top:85px;width:82px;height:62px;background:var(--brand);border-radius:0 3px 3px 0;box-shadow:0 3px 8px rgba(232,20,28,.3);display:flex;align-items:center;justify-content:center}
.nav-icon{position:absolute;left:22px;width:28px;height:28px}
.card{position:absolute;background:var(--card);border-radius:5px;box-shadow:0 1px 4px rgba(0,0,0,.04)}
.activities{left:110px;top:91px;width:625px;height:873px}
.card-title{position:absolute;left:26px;font-size:17.5px;font-weight:400;color:var(--ink)}
.activity{position:absolute;left:0;width:625px}
.activity .avatar{position:absolute;left:26px;top:0;width:35px;height:35px;border-radius:50%;background:linear-gradient(135deg,#9aa3aa,#4f565d)}
.activity .head{position:absolute;left:70px;top:2px;display:flex;align-items:center;font-size:12.5px}
.activity .author{color:var(--brand);font-size:16px;font-weight:400}
.activity .sep{width:1px;height:16px;background:var(--brand);margin:0 7px}
.activity .team{color:var(--brand)}
.activity .when{position:absolute;right:24px;top:6px;font-size:11px;color:var(--soft)}
.activity .subject{position:absolute;left:70px;top:27px;font-size:11px;color:var(--soft)}
.activity .body{position:absolute;left:70px;top:46px;width:520px;font-size:12.4px;line-height:21px;font-weight:300;color:var(--muted)}
.divider{position:absolute;left:0;width:100%;height:1px;background:var(--line)}
.events{left:763px;top:91px;width:324px;height:291px}
.tasks{left:763px;top:405px;width:324px;height:290px}
.polls{left:763px;top:715px;width:326px;height:249px}
.more{position:absolute;left:0;width:100%;text-align:center;font-size:14px;letter-spacing:2px;color:#8b9099;line-height:1}
.timeline{position:absolute;left:27px;top:60px;width:1px;height:231px;background:var(--line)}
.event{position:absolute;left:0;width:324px}
.event .dot{position:absolute;left:24px;top:5px;width:8px;height:8px;border-radius:50%;background:var(--brand)}
.event .dot.amber{background:var(--amber)}
.event .date{position:absolute;left:41px;top:0;font-size:14px;color:var(--soft)}
.event .what{position:absolute;left:41px;top:19px;font-size:12.5px;color:var(--muted)}
.event .time{position:absolute;right:9px;top:4px;font-size:11px;color:var(--muted);text-align:right}
.event .place{position:absolute;right:9px;top:19px;font-size:8px;color:var(--muted)}
.day-label{position:absolute;left:26px;font-size:11px;font-weight:500;color:var(--ink)}
.task{position:absolute;left:26px;width:270px;height:35px}
.task .box{position:absolute;left:0;top:0;width:35px;height:35px;border-radius:3px;display:flex;align-items:center;justify-content:center}
.task .box.done{background:var(--brand-deep)}
.task .box.open{background:var(--green)}
.task .name{position:absolute;left:49px;top:3px;font-size:12.5px;color:var(--ink)}
.task .at{position:absolute;left:49px;top:20px;font-size:11px;color:var(--soft)}
.task .menu{position:absolute;right:-8px;top:8px;font-size:12px;color:#b6bbc3;letter-spacing:1px}
.question{position:absolute;left:27px;top:54px;font-size:12.5px;color:var(--soft)}
.grid-line{position:absolute;top:88px;width:1px;height:104px;background:var(--line)}
.bar{position:absolute;left:26px;height:6px;border-radius:3px}
.bar-label{position:absolute;font-size:12.5px;color:var(--ink)}
</style>
</head>
<body>
<header class="topbar">
  <div class="brand">Tablehub</div>
  <svg class="bell" width="24" height="28" viewBox="0 0 24 28" fill="none" stroke="#2b2d33" stroke-width="1.4"><path d="M5 19V12a7 7 0 0 1 14 0v7l2 2H3z"/><path d="M10 24a2 2 0 0 0 4 0"/><circle cx="18" cy="6" r="3" fill="#e8141c" stroke="none"/></svg>
  <svg class="gear" width="27" height="27" viewBox="0 0 24 24" fill="none" stroke="#2b2d33" stroke-width="1.3"><circle cx="12" cy="12" r="3.5"/><path d="M12 2l1.6 2.6 3-.8.6 3 3 .9-.9 3L21.8 12l-2.5 1.9.9 3-3 .9-.6 3-3-.8L12 22l-1.6-2.6-3 .8-.6-3-3-.9.9-3L2.2 12l2.5-1.9-.9-3 3-.9.6-3 3 .8z"/></svg>
  <div class="user-name">Daniel Marsh</div>
  <div class="user-avatar" role="img" aria-label="Profile photo of the signed-in user"></div>
</header>

<nav class="sidebar">
  <div class="nav-home" style="top:20px">
    <svg width="32" height="30" viewBox="0 0 32 30" fill="none" stroke="#fff" stroke-width="1.8"><path d="M3 14L16 3l13 11"/><path d="M7 11v16h18V11"/><path d="M13 27v-8h6v8"/></svg>
  </div>
  <svg class="nav-icon" style="top:116px" viewBox="0 0 28 28" fill="none" stroke="#c5c9cf" stroke-width="1.2"><rect x="3" y="3" width="22" height="12" rx="1"/><path d="M7 8h14M7 11h9"/><path d="M6 22l1-2 1 2 2 .2-1.6 1.3.5 2-1.9-1-1.9 1 .5-2L4 22.2zM14 22l1-2 1 2 2 .2-1.6 1.3.5 2-1.9-1-1.9 1 .5-2L12 22.2zM22 22l1-2 1 2 2 .2-1.6 1.3.5 2-1.9-1-1.9 1 .5-2L20 22.2z"/></svg>
  <svg class="nav-icon" style="top:172px" viewBox="0 0 28 28" fill="none" stroke="#c5c9cf" stroke-width="1.2"><path d="M4 22h20v3H4z"/><path d="M7 22l4-12h6l4 12"/><circle cx="14" cy="7" r="3"/></svg>
  <svg class="nav-icon" style="top:228px" viewBox="0 0 28 28" fill="none" stroke="#c5c9cf" stroke-width="1.2"><circle cx="14" cy="6" r="3"/><circle cx="6" cy="18" r="3"/><circle cx="22" cy="18" r="3"/><path d="M11 8l-4 7M17 8l4 7M9 19h10"/></svg>
  <svg class="nav-icon" style="top:285px" viewBox="0 0 28 28" fill="none" stroke="#c5c9cf" stroke-width="1.2"><rect x="3" y="5" width="22" height="20" rx="1"/><path d="M3 10h22M8 3v4M20 3v4M7 14h14M7 18h14M7 22h14M11 12v12M17 12v12"/></svg>
  <svg class="nav-icon" style="top:342px" viewBox="0 0 28 28" fill="none" stroke="#c5c9cf" stroke-width="1.2"><rect x="5" y="3" width="18" height="23" rx="1"/><path d="M8 9l1.5 1.5L12 8M14 9h6M8 15l1.5 1.5L12 14M14 15h6M8 21l1.5 1.5L12 20M14 21h6"/></svg>
  <svg class="nav-icon" style="top:398px" viewBox="0 0 28 28" fill="none" stroke="#c5c9cf" stroke-width="1.2"><path d="M4 10h20v15H4z"/><path d="M7 10V4h11l3 3v3"/><path d="M4 10l3 15"/></svg>
  <svg class="nav-icon" style="top:455px" viewBox="0 0 28 28" fill="none" stroke="#c5c9cf" stroke-width="1.4"><path d="M12 16l4-4"/><path d="M10 13l-4 4a3.5 3.5 0 0 0 5 5l4-4"/><path d="M18 15l4-4a3.5 3.5 0 0 0-5-5l-4 4"/></svg>
</nav>

<section class="card activities">
  <h2 class="card-title" style="top:28px">Recent Activities</h2>

  <article class="activity" style="top:93px">
    <div class="avatar" role="img" aria-label="Author profile photo"></div>
    <div class="head"><span class="author">Daniel Marsh</span><span class="sep"></span><span>Public Post</span></div>
    <div class="when">Today at 1:34pm</div>
    <div class="subject">Post Subject Message</div>
    <p class="body">Lorem ipsum dolor sit amet, sit periculis signiferumque an, no duo sint meis contentiones. Vel alii congue abhorreant te. Nam altera putent gloriatur no. Augue eligendi neglegentur usu ea, dolor dicunt dignissim in usu. Cu debitis impedit detracto eam, integre disputationi eos ut.</p>
  </article>
  <div class="divider" style="top:230px"></div>

  <article class="activity" style="top:271px">
    <div class="avatar" role="img" aria-label="Author profile photo"></div>
    <div class="head"><span class="author">Daniel Marsh</span><span class="sep"></span><span>Private Post - </span><span class="team">&nbsp;Team Leaders</span></div>
    <div class="when">Yesterday at 4:14pm</div>
    <div class="subject">Post Subject Message</div>
    <p class="body">Lorem ipsum dolor sit amet, sit periculis signiferumque an, no duo sint meis contentiones. Vel alii congue abhorreant te. Nam altera putent gloriatur no. Augue eligendi neglegentur usu ea, dolor dicunt dignissim in usu. Cu debitis impedit detracto eam, integre disputationi eos ut.</p>
  </article>
  <div class="divider" style="top:400px"></div>

  <article class="activity" style="top:421px">
    <div class="avatar" role="img" aria-label="Author profile photo"></div>
    <div class="head"><span class="author">Daniel Marsh</span><span class="sep"></span><span>Private Post - </span><span class="team">&nbsp;Team Leaders</span></div>
    <div class="when">Yesterday at 4:14pm</div>
    <div class="subject">Performance Review for Daniel Marsh</div>
    <p class="body">Lorem ipsum dolor sit amet, sit periculis signiferumque an, no duo sint meis contentiones. Vel alii congue abhorreant te. Nam altera putent gloriatur no. Augue eligendi neglegentur usu ea, dolor dicunt dignissim in usu. Cu debitis impedit detracto eam, integre disputationi eos ut.</p>
  </article>
  <div class="divider" style="top:554px"></div>

  <article class="activity" style="top:575px">
    <div class="avatar" role="img" aria-label="Author profile photo"></div>
    <div class="head"><span class="author">Daniel Marsh</span><span class="sep"></span><span>Private Post - </span><span class="team">&nbsp;Team Leaders</span></div>
    <div class="when">Yesterday at 4:14pm</div>
    <div class="subject">Performance Review for Daniel Marsh</div>
    <p class="body">Lorem ipsum dolor sit amet, sit periculis signiferumque an, no duo sint meis contentiones. Vel alii congue abhorreant te. Nam altera putent gloriatur no. Augue eligendi neglegentur usu ea, dolor dicunt dignissim in usu. Cu debitis impedit detracto eam, integre disputationi eos ut.</p>
  </article>
  <div class="divider" style="top:712px"></div>

  <article class="activity" style="top:739px">
    <div class="avatar" role="img" aria-label="Author profile photo"></div>
    <div class="head"><span class="author">Daniel Marsh</span><span class="sep"></span><span>Private Post - </span><span class="team">&nbsp;Team Leaders</span></div>
    <div class="when">Yesterday at 4:14pm</div>
    <div class="subject">Performance Review for Daniel Marsh</div>
    <p class="body">Lorem ipsum dolor sit amet, sit periculis signiferumque an, no duo sint meis contentiones. Vel alii congue abhorreant te. Nam altera putent gloriatur no. Augue eligendi neglegentur usu ea, dolor dicunt dignissim in usu. Cu debitis impedit detracto eam, integre disputationi eos ut.</p>
  </article>
</section>

<section class="card events">
  <h2 class="card-title" style="top:25px">Events</h2>
  <div class="divider" style="top:60px;left:9px;width:315px"></div>
  <div class="timeline"></div>
  <div class="event" style="top:87px"><span class="dot"></span><div class="date">Jan 23</div><div class="what">Director Meeting</div><div class="time">8:30 AM - 9:30 AM</div><div class="place">Restaurant</div></div>
  <div class="event" style="top:143px"><span class="dot"></span><div class="date">Jan 28</div><div class="what">Director Meeting</div><div class="time">9:30 AM - 10:00 AM</div><div class="place">Breakfast</div></div>
  <div class="event" style="top:197px"><span class="dot amber"></span><div class="date">Jan 28</div><div class="what">Call with Northfield</div><div class="time">1:00 PM</div><div class="place">Conference Call</div></div>
  <div class="more" style="top:262px">•••</div>
</section>

<section class="card tasks">
  <h2 class="card-title" style="top:25px">Tasks</h2>
  <div class="divider" style="top:60px"></div>
  <div class="day-label" style="top:77px">TOMORROW - MARCH 4, 2019</div>
  <div class="task" style="top:105px">
    <div class="box done"><svg width="20" height="16" viewBox="0 0 20 16" fill="none" stroke="#fff" stroke-width="3"><path d="M2 8l5 5L18 2"/></svg></div>
    <div class="name">Daily Safe Checklist</div><div class="at">8:45 AM</div><div class="menu">•••</div>
  </div>
  <div class="task" style="top:154px">
    <div class="box open"><svg width="22" height="22" viewBox="0 0 22 22" fill="none" stroke="#fff" stroke-width="2.2"><path d="M18 8a8 8 0 1 0 1 4"/><path d="M19 3v5h-5"/></svg></div>
    <div class="name">Daily ERQA</div><div class="at">9:15 AM</div><div class="menu">•••</div>
  </div>
  <div class="day-label" style="top:205px">MARCH 5, 2019</div>
  <div class="task" style="top:226px">
    <div class="box open"><svg width="22" height="22" viewBox="0 0 22 22" fill="none" stroke="#fff" stroke-width="2.2"><path d="M18 8a8 8 0 1 0 1 4"/><path d="M19 3v5h-5"/></svg></div>
    <div class="name">Daily ERQA</div><div class="at">9:15 AM</div><div class="menu">•••</div>
  </div>
  <div class="more" style="top:270px">•••</div>
</section>

<section class="card polls">
  <h2 class="card-title" style="top:28px">Polls</h2>
  <div class="question">What is your favorite entree?</div>
  <div class="divider" style="top:88px"></div>
  <div class="grid-line" style="left:27px"></div>
  <div class="grid-line" style="left:96px"></div>
  <div class="grid-line" style="left:165px"></div>
  <div class="grid-line" style="left:234px"></div>
  <div class="bar" style="top:106px;width:181px;background:var(--cyan)"></div>
  <div class="bar-label" style="left:216px;top:100px">Fish Burger</div>
  <div class="bar" style="top:140px;width:119px;background:var(--orange)"></div>
  <div class="bar-label" style="left:155px;top:134px">Chicken Stripes</div>
  <div class="divider" style="top:192px"></div>
  <div class="more" style="top:218px">•••</div>
</section>
</body>
</html>
```